Business Card Design Project - Sports Brand

Lumora is a e-commerce fitness wear brand for ladies who are into gym, pole and swim.

Card should not be overly cluttered and should include the following:

1. logo
2. Name of the company (Use "Lumora Wear Pte Ltd" for now)
3. Address of company (Use a mock address)
4. Representative's name and contact info etc. (use a mock name and contact info)
5. website address

Target Market(s)

Women who are into pole , gym, and swim.

Women who shop online

Industry/Entity Type

E-Commerce

Colors

Designer to choose colors to be used in the design.

Requirements
Nice to have
• feminine sublimation of colours

Need not be printed on traditional paper. We would like the design to be revolutionary and interesting to the eye :)
Should not have
• the design should not be traditional looking. Do not include illustrations of Bikinis, yoga poses etc. in the card.

```html
<!DOCTYPE html>
<html lang="en">
<head>
<meta charset="utf-8">
<title>Lumora Wear – Business Card</title>
<link rel="stylesheet" href="https://fonts.googleapis.com/css2?family=Questrial&display=swap">
<style>
  :root {
    --stage: #ececec;
    --paper: #f7f7f6;
    --brand-red: #b3262e;
    --card-red-deep: #b5202b;
    --card-red-mid: #d3412d;
    --card-orange: #ea6a2c;
    --wash-pink: #e8559a;
    --wash-rose: #f07ab2;
    --wash-orange: #f27a3c;
    --ink-light: #ffffff;
    --ink-soft: #f6c9cc;
    --rule: rgba(255, 210, 210, 0.45);
    --ring: #f3b6cf;
  }
  * { box-sizing: border-box; margin: 0; padding: 0; }
  html, body {
    width: 1200px; height: 900px; overflow: hidden;
    background: var(--stage);
    font-family: "Questrial", "Century Gothic", sans-serif;
  }
  .stage {
    width: 1200px; height: 900px;
    display: flex; flex-direction: column;
    align-items: center; justify-content: center; gap: 48px;
  }
  .card {
    width: 660px; height: 377px; position: relative; overflow: hidden;
    border-radius: 4px;
    box-shadow: 0 6px 18px rgba(0,0,0,0.18);
  }

  /* Front */
  .card--front { background: var(--paper); }
  .card--front .wash {
    position: absolute; left: 210px; top: 88px;
    width: 200px; height: 200px; border-radius: 50%;
    background: radial-gradient(circle at 60% 60%, var(--wash-orange) 0%, var(--wash-pink) 48%, var(--wash-rose) 72%, rgba(240,122,178,0) 100%);
    opacity: 0.9;
  }
  .card--front .brand-name {
    position: absolute; left: 330px; top: 118px;
    font-size: 62px; color: var(--brand-red); letter-spacing: 1px;
  }

  /* Back */
  .card--back {
    background: radial-gradient(ellipse at 70% 35%, var(--card-orange) 0%, var(--card-red-mid) 45%, var(--card-red-deep) 100%);
    color: var(--ink-soft);
  }
  .badge {
    position: absolute; left: 50%; top: 26px; transform: translateX(-50%);
    width: 150px; height: 150px; border-radius: 50%;
    background: #ffffff; border: 3px solid var(--ring);
    display: flex; align-items: center; justify-content: center;
  }
  .badge .wash {
    position: absolute; left: 18px; top: 30px;
    width: 82px; height: 82px; border-radius: 50%;
    background: radial-gradient(circle at 60% 60%, var(--wash-orange) 0%, var(--wash-pink) 50%, rgba(240,122,178,0) 100%);
  }
  .badge .brand-name {
    position: relative; font-size: 30px; color: var(--brand-red); margin-left: 28px;
  }
  .company {
    position: absolute; top: 196px; left: 0; right: 0; text-align: center;
    font-size: 28px; color: var(--ink-light); letter-spacing: 0.5px;
  }
  .rule {
    position: absolute; top: 242px; left: 60px; right: 60px;
    height: 1px; background: linear-gradient(90deg, transparent, var(--rule), transparent);
  }
  .divider {
    position: absolute; top: 258px; left: 50%; width: 1px; height: 76px;
    background: var(--rule);
  }
  .details {
    position: absolute; top: 264px; width: 270px;
    font-size: 17px; line-height: 1.75; list-style: none;
  }
  .details--left { left: 50px; }
  .details--right { left: 356px; }
  .details li { display: flex; align-items: center; gap: 10px; }
  .details .icon { width: 14px; height: 14px; flex: none; fill: var(--ink-soft); }
  .details .icon--stroke { fill: none; stroke: var(--ink-soft); stroke-width: 1.4; }
  .rep { padding-left: 0; }
</style>
</head>
<body>
<main class="stage">
  <section class="card card--front" aria-label="Card front">
    <div class="wash" role="img" aria-label="Soft pink and orange watercolour wash behind the brand name"></div>
    <div class="brand-name">Lumora</div>
  </section>

  <section class="card card--back" aria-label="Card back">
    <div class="badge">
      <div class="wash" role="img" aria-label="Soft pink and orange watercolour wash"></div>
      <div class="brand-name">Lumora</div>
    </div>
    <h1 class="company" style="font-weight:400">Lumora Wear Pte Ltd</h1>
    <div class="rule"></div>
    <div class="divider"></div>
    <ul class="details details--left">
      <li class="rep">Representative's Name</li>
      <li>
        <svg class="icon" viewBox="0 0 14 14" aria-hidden="true"><path d="M7 0.5a4.5 4.5 0 0 0-4.5 4.5c0 3.3 4.5 8.5 4.5 8.5s4.5-5.2 4.5-8.5A4.5 4.5 0 0 0 7 0.5zm0 6.3a1.8 1.8 0 1 1 0-3.6 1.8 1.8 0 0 1 0 3.6z"/></svg>
        Your Address
      </li>
    </ul>
    <ul class="details details--right">
      <li>
        <svg class="icon" viewBox="0 0 14 14" aria-hidden="true"><path d="M3.2 0.8l2 2.6-1.2 1.5c.8 1.7 2.2 3.1 3.9 3.9l1.5-1.2 2.6 2-1.1 2.3C6.2 13.6.4 7.8.9 1.9z"/></svg>
        Your Contact Info
      </li>
      <li>
        <svg class="icon icon--stroke" viewBox="0 0 14 14" aria-hidden="true"><circle cx="7" cy="7" r="6"/><ellipse cx="7" cy="7" rx="2.6" ry="6"/><path d="M1 7h12M2 3.8h10M2 10.2h10"/></svg>
        Your Website Address
      </li>
    </ul>
  </section>
</main>
</body>
</html>
```